Poster for Dance Choreography Workshop

We need a poster for a dance workshop. This workshop is unique in that instead of focusing on dance technique or on classical compositional practices, it teaches participants a toolbox of a collaborative, improvisational methods for generating movement and creating dances.

The workshop is called VERIL (Methods for Exploring Gesture and Dancemaking). Our dance company is Helen Dorsey & Ensemble.

Here is copy:
VERIL (Methods for Exploring Gesture and Dancemaking) is a six-day intensive led by Helen Dorsey & Ensemble in which dancers and choreographers investigate collaborative approaches to choreography. Each day begins with an hour-long presentation during which Helen Dorsey leads discussions on topics related to choreography and collaboration. Following this, Helen Dorsey and VERIL company members teach a variety of practices for collaborative movement-making that merge improvisational skills with contemporary dance technique and physical theater. Using these practices, participants will create miniature compositions in small groups each day. By examining and discussing these creations, participants leave with greater confidence in their creative abilities and a deeper understanding of composition and movement-making.
This intensive, hosted at Whitcombe College in NYC, brings together a wide variety of talented dance artists and provides them with a supportive environment in which to play, learn, experiment and share. The intensive also affords an exciting opportunity for building peer-communities and forging new creative bonds. VERIL’s goal is that all participants leave with fresh perspectives, tools they can immediately use in their own rehearsals, and a better understanding of their own creative processes.

DATES:
June 11—June 16, 2012
10:00am—6:00pm daily
LOCATION:
Department of Dance,
Whitcombe College of
Harrowgate University
4127 Linden Avenue at 82nd
New York, NY 10094
Housing is not available.
Company teachers:
Helen Dorsey
Maribeth Quennell
Owen Patch
Toby Renfield

Special presentation by
Greta L. Fenwick,
Tall Stage Collective

Applications available online at www.helendorseyensemble.org or email veril@verilworks.org.
Application deadline April 1, 2012.

Hello all,

Nice work so far!
Please note that I have high resolution version of the images in the brief available. I did not include them because of the bandwidth of my connection. If you would like some of the images in higher res (5616x3744) let me know and I can provide them.

Best,

Colin

Target Market(s)

College-age and above. Professional dancers.

Industry/Entity Type

Environment

Requirements
Must have
• Poster must be 11x17 or smaller.
Visit www.northernmovementfair.org, www.pkthf.org, www.vlxmotion.org for competitors. Should not be easy to confuse with these.

```html
<!DOCTYPE html>
<html lang="en">
<head>
<meta charset="utf-8">
<title>Academy of Dance — VERIL Intensive</title>
<link rel="stylesheet" href="https://fonts.googleapis.com/css2?family=Mulish:wght@200;300;400;700&display=swap">
<style>
  :root {
    --backdrop: #ecebe8;
    --paper: #ffffff;
    --teal: #5bbdab;
    --teal-deep: #2f6f68;
    --teal-mid: #4a968c;
    --red: #d6432b;
    --red-text: #d8553c;
    --ink: #333333;
    --grey: #a3a3a3;
    --grey-dark: #555555;
  }
  * { box-sizing: border-box; margin: 0; padding: 0; }
  html, body { width: 1200px; height: 900px; overflow: hidden; }
  body {
    background: var(--backdrop);
    font-family: "Mulish", Arial, sans-serif;
    position: relative;
  }
  .poster {
    position: absolute;
    left: 330px; top: 26px;
    width: 568px; height: 856px;
    background: var(--paper);
    box-shadow: 0 2px 10px rgba(0,0,0,.18);
  }
  .hero {
    position: absolute;
    left: 13px; top: 14px;
    width: 538px; height: 248px;
    background: var(--teal);
  }
  .hero-photos {
    position: absolute;
    left: 17px; top: 16px;
    width: 506px; height: 202px;
    background: linear-gradient(135deg, var(--teal-deep) 0%, var(--teal-mid) 55%, #3c7f77 100%);
  }
  .title-top {
    position: absolute;
    left: 29px; top: 178px;
    font-weight: 200;
    font-size: 38px;
    line-height: 1;
    color: #fff;
    letter-spacing: -0.5px;
  }
  .title-box {
    position: absolute;
    left: 13px; top: 217px;
    width: 260px; height: 64px;
    background: var(--red);
  }
  .title-main {
    position: absolute;
    left: 28px; top: 219px;
    font-weight: 700;
    font-size: 58px;
    line-height: 1;
    color: #fff;
    letter-spacing: -1px;
  }
  .intro {
    position: absolute;
    top: 309px;
    width: 240px;
    font-size: 9.6px;
    line-height: 17px;
    color: var(--red-text);
  }
  .intro-left { left: 31px; }
  .intro-right { left: 287px; width: 260px; }
  .intro .lead { color: var(--ink); }
  .mission-lead {
    position: absolute;
    left: 30px; top: 496px;
    font-size: 7.6px;
    font-weight: 700;
    color: var(--red);
    white-space: nowrap;
  }
  .mission {
    position: absolute;
    left: 13px; top: 511px;
    width: 538px; height: 57px;
    background: var(--red);
    padding: 3px 17px 0;
    font-size: 7.6px;
    line-height: 17px;
    color: #fff;
  }
  .info {
    position: absolute;
    top: 613px;
  }
  .info-rule {
    height: 2px;
    background: linear-gradient(90deg, var(--red), var(--teal));
    margin-bottom: 9px;
  }
  .info h2 {
    font-weight: 300;
    font-size: 19px;
    line-height: 1;
    color: var(--ink);
    margin-bottom: 6px;
  }
  .info p {
    font-size: 9.4px;
    font-weight: 300;
    line-height: 15px;
    color: var(--grey);
  }
  .info-dates { left: 41px; width: 98px; }
  .info-location { left: 205px; width: 97px; }
  .info-teachers { left: 352px; width: 166px; }
  .info .special {
    margin-top: 11px;
    font-size: 6.2px;
    line-height: 7.5px;
    color: var(--grey-dark);
    font-weight: 400;
  }
  .footer {
    position: absolute;
    left: 13px; top: 784px;
    width: 538px; height: 62px;
    background: var(--teal);
    text-align: center;
    color: #fff;
    padding-top: 16px;
  }
  .footer-note { font-size: 7.4px; font-weight: 300; opacity: .9; }
  .footer-deadline { font-size: 13.5px; font-weight: 300; margin-top: 1px; }
</style>
</head>
<body>
  <main class="poster">
    <section class="hero">
      <div class="hero-photos" role="img" aria-label="Grid of teal-toned rehearsal photographs of dancers working together in a studio"></div>
    </section>
    <div class="title-box"></div>
    <h1>
      <span class="title-top">Academy of</span>
      <span class="title-main">Dance</span>
    </h1>

    <p class="intro intro-left"><span class="lead">VERIL (Methods for Exploring Gesture and Dancemaking)</span> is a six-day intensive led by Helen Dorsey &amp; Ensemble in which dancers and choreographers investigate collaborative approaches to choreography. Each day begins with an hour-long presentation during which Helen Dorsey leads discussions on topics related to choreography and collaboration. Following this, Helen Dorsey and VERIL company members teach a</p>
    <p class="intro intro-right">variety of practices for collaborative movement-making that merge improvisational skills with contemporary dance technique and physical theater. Using these practices, participants will create miniature compositions in small groups each day.<br>By examining and discussing these creations, participants leave with greater confidence in their creative abilities and a deeper understanding of composition and movement-making.</p>

    <p class="mission-lead">This intensive, hosted at Whitcombe College in NYC, brings together a wide variety of talented dance artists and provides them</p>
    <p class="mission">a supportive environment in which to play, learn, experiment and share. The intensive also affords an exciting opportunity for building peer-communities and forging new creative bonds. VERIL’s goal is that all participants leave with fresh perspectives, tools they can immediately use in their own rehearsals, and a better understanding of their own creative processes.</p>

    <section class="info info-dates">
      <div class="info-rule"></div>
      <h2>Dates:</h2>
      <p>June 11- June 16, 2012<br>10:00am - 6:00pm daily</p>
    </section>
    <section class="info info-location">
      <div class="info-rule"></div>
      <h2>Location:</h2>
      <p>Department of Dance,<br>Whitcombe College of<br>Harrowgate University<br>4127 Linden Avenue at 82nd<br>New York, NY 10094</p>
    </section>
    <section class="info info-teachers">
      <div class="info-rule"></div>
      <h2>Company teachers:</h2>
      <p>Helen Dorsey<br>Maribeth Quennell<br>Owen Patch<br>Toby Renfield</p>
      <p class="special">Special presentation by<br>Greta L. Fenwick,<br>Tall Stage Collective</p>
    </section>

    <footer class="footer">
      <p class="footer-note">Applications available online at www.helendorseyensemble.org or email veril@verilworks.org.</p>
      <p class="footer-deadline">Application deadline April 1, 2012</p>
    </footer>
  </main>
</body>
</html>
```